Business card design Needed for new logo / Construction business, home extensions and new builds

We need a business card design using our new logo files which i will attach to this project :)

We are a small construction business specialising in home extensions, new builds and property development. We are very ambitious and would appreciate professional and elegant designs for our new business card.

Very serious about using the services on Sketchwharf and recently acquired our new logo from here :)

Please get involved, i will feedback when i can as i am very busy but can respond daily, thanks

Target Market(s)

People that want to build onto their houses, new building developments or adding too their existing property

Industry/Entity Type

Construction

Contact Information for Business Card

Thornley Pike Construction, Wilbur Fenwick (Managing Director), Tel 07829456172, email - info@thornley-pike, www.thornley-pike.co.uk

Colors

Designer to choose colors to be used in the design.

Requirements
Must have
• I like a deep grey on the back please. A lot of you have provided black from and back, try mixing things up a little. The black looks cool 😎 Thanks

```html
<!DOCTYPE html>
<html lang="en">
<head>
<meta charset="utf-8">
<title>Thornley Pike Construction – Business Card</title>
<link rel="stylesheet" href="https://fonts.googleapis.com/css2?family=Lato:wght@400;700&display=swap">
<style>
  :root {
    --page: #2b2b2c;
    --card: #454546;
    --gold: #d9a632;
    --gold-deep: #b27a14;
    --gold-light: #f3d27a;
    --silver: #c9cbce;
    --silver-deep: #8c9096;
    --ink-dark: #2a2a2a;
  }
  * { box-sizing: border-box; margin: 0; padding: 0; }
  html, body { width: 1200px; height: 982px; overflow: hidden; }
  body {
    background: var(--page);
    font-family: "Lato", sans-serif;
    position: relative;
  }
  .card {
    position: absolute;
    width: 640px;
    height: 366px;
    background: var(--card);
    border-radius: 22px;
    overflow: hidden;
    box-shadow: 0 10px 30px rgba(0,0,0,.35);
  }
  .card--front { left: 460px; top: 60px; }
  .card--back  { left: 100px; top: 540px; }

  .brand-name {
    font-family: "Lato", sans-serif;
    font-weight: 700;
    color: var(--gold);
    text-transform: uppercase;
    text-align: center;
    letter-spacing: 2px;
    line-height: 1.15;
  }
  .brand-mark {
    display: block;
    background: var(--gold);
    border-radius: 50%;
    margin: 0 auto;
  }
  .card--front .brand {
    position: absolute;
    left: 0; right: 0; top: 92px;
  }
  .card--front .brand-mark { width: 64px; height: 64px; margin-bottom: 26px; }
  .card--front .brand-name { font-size: 34px; }

  .card--back .brand {
    position: absolute;
    right: 36px; top: 96px;
    width: 250px;
  }
  .card--back .brand-mark { width: 44px; height: 44px; margin-bottom: 16px; }
  .card--back .brand-name { font-size: 20px; }

  .contact {
    position: absolute;
    left: 44px; top: 96px;
  }
  .contact-name {
    color: var(--gold);
    font-size: 28px;
    font-weight: 400;
    text-transform: uppercase;
    letter-spacing: .5px;
  }
  .contact-role {
    color: #e6e6e6;
    font-size: 19px;
    margin-top: 2px;
  }
  .contact-rule {
    width: 300px;
    height: 2px;
    background: var(--gold);
    margin: 14px 0 14px;
  }
  .contact-line {
    display: flex;
    align-items: center;
    gap: 12px;
    color: #ececec;
    font-size: 19px;
    margin-bottom: 8px;
  }
  .contact-line svg { width: 18px; height: 18px; flex: none; }

  .web-band {
    position: absolute;
    left: 0; bottom: 0;
    width: 100%;
    height: 58px;
  }
  .web-band__gold {
    position: absolute;
    left: 0; top: 0; bottom: 0;
    width: 86%;
    background: linear-gradient(90deg, var(--gold-deep), var(--gold-light) 45%, var(--gold) 70%, var(--gold-deep));
    clip-path: polygon(0 0, 96% 0, 100% 100%, 0 100%);
  }
  .web-band__silver {
    position: absolute;
    right: 0; top: 0; bottom: 0;
    width: 16%;
    background: linear-gradient(90deg, #f1f2f3, var(--silver) 50%, var(--silver-deep));
    clip-path: polygon(0 0, 100% 0, 100% 100%, 14% 100%);
  }
  .web-band__text {
    position: absolute;
    left: 190px; top: 0; bottom: 0;
    display: flex; align-items: center;
    color: var(--ink-dark);
    font-size: 18px;
    font-weight: 700;
    letter-spacing: 3px;
    text-transform: uppercase;
  }
</style>
</head>
<body>

  <section class="card card--front" aria-label="Card front">
    <div class="brand">
      <span class="brand-mark"></span>
      <p class="brand-name">Thornley Pike<br>Construction</p>
    </div>
  </section>

  <section class="card card--back" aria-label="Card back">
    <div class="contact">
      <h1 class="contact-name">Wilbur Fenwick</h1>
      <p class="contact-role">Managing Director</p>
      <div class="contact-rule"></div>
      <p class="contact-line">
        <svg viewBox="0 0 24 24" aria-hidden="true"><path fill="#d9a632" d="M6.6 10.8a15.1 15.1 0 0 0 6.6 6.6l2.2-2.2c.3-.3.7-.4 1-.2 1.1.4 2.3.6 3.6.6.6 0 1 .4 1 1V20c0 .6-.4 1-1 1A17 17 0 0 1 3 4c0-.6.4-1 1-1h3.5c.6 0 1 .4 1 1 0 1.3.2 2.5.6 3.6.1.3 0 .7-.2 1z"/></svg>
        07829456172
      </p>
      <p class="contact-line">
        <svg viewBox="0 0 24 24" aria-hidden="true"><path fill="#d9a632" d="M2 5h20v14H2z"/><path fill="none" stroke="#454546" stroke-width="1.8" d="M2.5 5.5 12 13l9.5-7.5"/></svg>
        info@thornley-pike.co.uk
      </p>
    </div>

    <div class="brand">
      <span class="brand-mark"></span>
      <p class="brand-name">Thornley Pike<br>Construction</p>
    </div>

    <div class="web-band">
      <div class="web-band__gold"></div>
      <div class="web-band__silver"></div>
      <p class="web-band__text">www.thornley-pike.co.uk</p>
    </div>
  </section>

</body>
</html>
```